Email signature banner for companys 60th anniversary

We are a transportation company. This is what our website people came up with so far:

https://www.plavemockups.com/design/8xWq2LpZr4TnBv7KcYdMfA/Bornel?node-id=4417-35

I want a picture of our transport truck with the decal on the back that we are putting on it.

Our website is www.bornel.com

Target Market(s)

Customer recognition

Industry/Entity Type

fuel and oil distribution company

Requirements
Must have
• our 60th anniversary logo
Nice to have
• Delivering Energy to Build Communites.
Should not have
• picture of the guy from the current banner provided

```html
<!DOCTYPE html>
<html lang="en">
<head>
<meta charset="utf-8">
<title>Bornel 60th Anniversary Email Banner</title>
<link rel="stylesheet" href="https://fonts.googleapis.com/css2?family=Roboto+Condensed:wght@700&display=swap">
<style>
  :root {
    --artboard: #63666a;
    --brand-red: #e11b22;
    --brand-navy: #0f3a85;
    --blue-deep: #2b4a92;
    --blue-mid: #3560ac;
    --blue-light: #4a8ddb;
    --white: #ffffff;
    --photo-sky: #8fa9cf;
    --photo-steel: #c9ced6;
    --photo-road: #7d8a9b;
  }
  * { margin: 0; padding: 0; box-sizing: border-box; }
  html, body {
    width: 1200px;
    height: 630px;
    overflow: hidden;
    background: var(--artboard);
  }
  .banner {
    position: absolute;
    left: 76px;
    top: 181px;
    width: 1048px;
    height: 268px;
    overflow: hidden;
    background: linear-gradient(90deg, var(--blue-deep) 0%, var(--blue-deep) 45%, var(--blue-mid) 70%, var(--blue-light) 100%);
    font-family: "Roboto Condensed", "Arial Narrow", sans-serif;
    font-weight: 700;
    color: var(--white);
  }
  .tagline-band {
    position: absolute;
    inset: 0;
    width: 100%;
    height: 68px;
  }
  .tagline {
    position: absolute;
    right: 17px;
    top: 9px;
    font-size: 39px;
    line-height: 48px;
    letter-spacing: 0.2px;
    white-space: nowrap;
  }
  .truck-photo {
    position: absolute;
    left: 0;
    top: 0;
    width: 620px;
    height: 268px;
    background:
      linear-gradient(180deg, rgba(255,255,255,0) 60%, var(--photo-road) 100%),
      linear-gradient(100deg, var(--blue-mid) 0%, var(--photo-sky) 18%, var(--photo-steel) 38%, var(--photo-steel) 55%, var(--photo-sky) 75%, rgba(53,96,172,0) 100%);
    -webkit-mask-image: linear-gradient(90deg, #000 70%, transparent 100%);
            mask-image: linear-gradient(90deg, #000 70%, transparent 100%);
  }
  .headline {
    position: absolute;
    left: 476px;
    top: 112px;
    text-transform: uppercase;
  }
  .headline-lead {
    display: block;
    font-size: 47px;
    line-height: 42px;
    letter-spacing: -0.3px;
  }
  .headline-main {
    display: block;
    font-size: 68px;
    line-height: 62px;
    letter-spacing: -0.5px;
  }
  .brand-mark {
    position: absolute;
    left: 776px;
    top: 108px;
    width: 250px;
    height: 100px;
    display: flex;
    align-items: center;
    gap: 12px;
  }
  .brand-dot {
    width: 30px;
    height: 30px;
    border-radius: 50%;
    background: var(--brand-red);
    flex: none;
  }
  .brand-name {
    font-size: 64px;
    line-height: 1;
    color: var(--brand-navy);
    text-transform: uppercase;
  }
</style>
</head>
<body>
  <div class="banner">
    <div class="truck-photo" role="img" aria-label="Rear view of a silver fuel tanker truck on a highway, with the 60th anniversary decal on the back of the tank"></div>

    <svg class="tagline-band" viewBox="0 0 1048 68" preserveAspectRatio="none" aria-hidden="true">
      <polygon points="250,0 1048,0 1048,66 402,66" fill="var(--brand-red)"/>
      <line x1="402" y1="67" x2="1048" y2="67" stroke="var(--white)" stroke-width="2"/>
    </svg>
    <p class="tagline">Delivering Energy to Build Communites</p>

    <h1 class="headline">
      <span class="headline-lead">Celebrating</span>
      <span class="headline-main">60 Years</span>
    </h1>

    <div class="brand-mark">
      <span class="brand-dot"></span>
      <span class="brand-name">Bornel</span>
    </div>
  </div>
</body>
</html>
```